New Webpage for High Class Expert Witness Services Company

We are looking for a minimalist design for a webpage that just has our logo and an entry form offer to connect with one of our Liaisons.
The entry form should just ask for Name, Email, Contact Info and Description of Project.

Company Name is: The Marlow Crest Advisory Services

Number of Pages Required

1 page

```html
<!DOCTYPE html>
<html lang="en">
<head>
<meta charset="utf-8">
<title>Get in Touch – Marlow Crest Advisory Services</title>
<link rel="stylesheet" href="https://fonts.googleapis.com/css2?family=Unbounded:wght@800&family=Urbanist:wght@400;700&family=Cinzel:wght@400&display=swap">
<style>
  :root {
    --bg: #000000;
    --bg-glow: #1a1a1a;
    --footer-bg: #111111;
    --text: #ffffff;
    --muted: #9a9a9a;
    --placeholder: #a8a8a8;
    --field-border: #bdbdbd;
    --field-active: #1b1b1b;
    --heading-top: #f4f4f4;
    --heading-bottom: #a6a6aa;
    --btn-start: #9a9a9c;
    --btn-end: #2a2a2c;
  }
  * { box-sizing: border-box; margin: 0; padding: 0; }
  html, body { width: 1200px; height: 675px; overflow: hidden; background: var(--bg); }
  body { position: relative; font-family: "Urbanist", sans-serif; color: var(--text); }

  .backdrop {
    position: absolute; inset: 0 0 50px 0;
    background: radial-gradient(ellipse 360px 300px at 593px 370px, var(--bg-glow) 0%, #0b0b0b 45%, var(--bg) 100%);
  }

  .brand {
    position: absolute; top: 47px; left: 0; width: 1200px;
    display: flex; justify-content: center; align-items: center; gap: 14px;
  }
  .brand-mark { width: 40px; height: 40px; background: #d0d0d0; }
  .brand-name {
    font-family: "Cinzel", serif; font-weight: 400; font-size: 24px;
    letter-spacing: 1.5px; color: #d6d6d6; line-height: 1.1;
  }

  .title {
    position: absolute; top: 170px; left: 0; width: 1200px; text-align: center;
    font-family: "Unbounded", sans-serif; font-weight: 800; font-size: 78px;
    letter-spacing: -1px; line-height: 1;
    background: linear-gradient(to bottom, var(--heading-top), var(--heading-bottom));
    -webkit-background-clip: text; background-clip: text; color: transparent;
  }

  .contact-form { position: absolute; top: 272px; left: 176px; width: 848px; }
  .field-row { display: flex; gap: 27px; }
  .field {
    width: 265px; height: 44px; padding: 0 17px;
    background: transparent; border: 1px solid var(--field-border);
    font-family: "Urbanist", sans-serif; font-size: 13.5px; color: var(--text);
    outline: none;
  }
  .field::placeholder, .message::placeholder { color: var(--placeholder); opacity: 1; }
  .field--active { background: var(--field-active); }
  .field--active::placeholder { color: var(--text); }
  .message {
    display: block; margin-top: 26px; width: 848px; height: 133px;
    padding: 14px 17px; resize: both;
    background: transparent; border: 1px solid var(--field-border);
    font-family: "Urbanist", sans-serif; font-size: 13.5px; color: var(--text);
    outline: none;
  }
  .submit {
    display: flex; align-items: center; justify-content: center; gap: 10px;
    margin: 26px 0 0 306px; width: 202px; height: 44px; border: none;
    background: linear-gradient(to right, var(--btn-start), var(--btn-end));
    font-family: "Urbanist", sans-serif; font-weight: 700; font-size: 14px;
    color: var(--text); letter-spacing: 0.3px; cursor: pointer;
  }

  .site-footer {
    position: absolute; left: 0; bottom: 0; width: 1200px; height: 50px;
    background: var(--footer-bg); display: flex; align-items: center; justify-content: center;
    font-size: 14px; color: var(--muted);
  }
</style>
</head>
<body>
  <div class="backdrop" role="img" aria-label="Dark digital security emblem with circular interface rings in the background"></div>

  <header class="brand">
    <span class="brand-mark"></span>
    <span class="brand-name">MARLOW CREST ADVISORY SERVICES</span>
  </header>

  <h1 class="title">GET IN TOUCH</h1>

  <form class="contact-form">
    <div class="field-row">
      <input class="field field--active" type="text" placeholder="NAME">
      <input class="field" type="email" placeholder="EMAIL">
      <input class="field" type="tel" placeholder="PHONE NUMBER">
    </div>
    <textarea class="message" placeholder="TELL US ABOUT YOUR PROJECT"></textarea>
    <button class="submit" type="button">SUBMIT REQUEST
      <svg width="24" height="10" viewBox="0 0 24 10" fill="none" stroke="#ffffff" stroke-width="1.4" aria-hidden="true">
        <line x1="0" y1="5" x2="22.5" y2="5"/>
        <polyline points="18,1 22.5,5 18,9"/>
      </svg>
    </button>
  </form>

  <footer class="site-footer">Copyright © 2026 - Marlow Crest Advisory Services</footer>
</body>
</html>
```